Industrial Company needing new business cards

We are a newly branded Industrial trade company. We specialise in Electrical, Mechanical and Air-conditioning.

I would like to see designs single sided. Focusing on the color scheme white/red/black and possibly gray. Possibly make it a black card with white writting... but open to all designs.

I would like the design to be professional, sleek and to the point.

Industry/Entity Type

Business

Contact Information for Business Card

Tom Harwick
Managing Director / Electrician
tomwork@velnet.com.au
47 Garnet Road, Rutherford NSW 2320
Mobile: 0427115830
www.harwickindustrialgroup.com.au

Requirements
Must have
• Must be able to be sent in a manner that i can change the details for each employee.
• Our logo
Nice to have
• Would like it to somehow have " incorporating Talvo Group Pty Ltd" as this is the company we have taken over.
Should not have
• No yellow!!!
• must not simply place "talvo group" randomly on the business card. refer nice to have.

```html
<!DOCTYPE html>
<html lang="en">
<head>
<meta charset="utf-8">
<title>Harwick Industrial Group – Business Card</title>
<link href="https://fonts.googleapis.com/css2?family=Source+Sans+3:wght@400;600;700&display=swap" rel="stylesheet">
<style>
  :root {
    --stage: #000000;
    --card: #2f3032;
    --card-light: #353638;
    --accent: #e3101b;
    --ink: #ffffff;
    --muted: #8d8e90;
  }
  * { box-sizing: border-box; margin: 0; padding: 0; }
  html, body { width: 1200px; height: 900px; overflow: hidden; background: var(--stage); }
  body { position: relative; font-family: "Source Sans 3", "Myriad Pro", Arial, sans-serif; color: var(--ink); }

  .card {
    position: absolute;
    top: 271px;
    width: 457px;
    height: 281px;
    border-radius: 14px;
    background: linear-gradient(135deg, var(--card-light) 0%, var(--card) 55%, #2b2c2e 100%);
    overflow: hidden;
  }
  .card--front { left: 137px; }
  .card--back { left: 626px; width: 458px; }

  .brand-name {
    position: absolute;
    left: 35px;
    top: 92px;
    font-size: 40px;
    font-weight: 700;
    letter-spacing: 1px;
    color: var(--ink);
    line-height: 1;
  }

  .person { position: absolute; right: 30px; top: 25px; text-align: right; }
  .person__name { font-size: 17px; font-weight: 600; color: var(--accent); line-height: 1.15; }
  .person__role { font-size: 13px; color: var(--ink); line-height: 1.4; }

  .address { position: absolute; right: 30px; top: 145px; text-align: right; font-size: 13px; line-height: 18px; font-style: normal; }

  .contacts { position: absolute; right: 30px; top: 199px; list-style: none; }
  .contacts li {
    display: flex; justify-content: flex-end; align-items: center;
    gap: 3px; font-size: 13px; height: 18.5px;
  }
  .contact-icon {
    width: 13px; height: 13px; border-radius: 2px;
    background: var(--accent);
    display: inline-flex; align-items: center; justify-content: center;
  }
  .contact-icon svg { width: 9px; height: 9px; }

  .lockup { position: absolute; left: 0; right: 0; top: 110px; text-align: center; }
  .lockup__name { font-size: 23px; font-weight: 700; letter-spacing: 1px; color: var(--ink); line-height: 1; }
  .lockup__services { margin-top: 30px; font-size: 9.5px; font-weight: 600; letter-spacing: 0.6px; color: var(--muted); line-height: 1; }

  .parent-company { position: absolute; left: 0; right: 0; top: 218px; text-align: center; font-size: 13px; }
</style>
</head>
<body>

<section class="card card--front" aria-label="Card front">
  <div class="brand-name">HARWICK</div>

  <div class="person">
    <p class="person__name">Tom Harwick</p>
    <p class="person__role">Managing Director / Electrician</p>
  </div>

  <address class="address">
    47 Garnet Road,<br>Kelvale NSW 2341
  </address>

  <ul class="contacts">
    <li>0427115830
      <span class="contact-icon"><svg viewBox="0 0 10 10"><path d="M2 1h2l1 2.5-1.2.8a5 5 0 0 0 2 2L6.6 5 9 6v2a1 1 0 0 1-1 1A7 7 0 0 1 1 2a1 1 0 0 1 1-1z" fill="#fff"/></svg></span>
    </li>
    <li>tomwork@velnet.com.au
      <span class="contact-icon"><svg viewBox="0 0 10 10"><rect x="1" y="2.5" width="8" height="5.5" fill="#fff"/><path d="M1 2.5l4 3 4-3" stroke="#e3101b" stroke-width="0.9" fill="none"/></svg></span>
    </li>
    <li>www.harwickindustrialgroup.com.au
      <span class="contact-icon"><svg viewBox="0 0 10 10"><path d="M4.2 5.8l1.6-1.6M3.5 4.5L2.4 5.6a1.4 1.4 0 0 0 2 2l1.1-1.1M6.5 5.5l1.1-1.1a1.4 1.4 0 0 0-2-2L4.5 3.5" stroke="#fff" stroke-width="1.1" fill="none" stroke-linecap="round"/></svg></span>
    </li>
  </ul>
</section>

<section class="card card--back" aria-label="Card back">
  <div class="lockup">
    <p class="lockup__name">HARWICK INDUSTRIAL GROUP</p>
    <p class="lockup__services">ELECTRICAL - MECHANICAL - AIRCONDITIONING</p>
  </div>
  <p class="parent-company">Talvo Group Pty Ltd</p>
</section>

</body>
</html>
```